Vegan Jerky company needs a label for it's pouch, and a new logo

Dear Designers - this used to be a guaranteed project, however, due to the low quality of designs I have received, I have removed the guaranteed status. However, we need this product made and we will pay for a great, high quality design that meets the requirements of our brief.

We need sticker labels that will go onto the front and back of our vegan jerky package. Our package is a zip-sealable pouch, and we will either go with black, white or brown for the color of the pouch.

We need the concept, artwork, theme and logo designed. Pls choose the colors.

There will be four flavors. These can be finished as part of another project. The flavors are: Smoked Maple, Cracked Pepper, Teriyaki Sriracha, Original.

We are Lonny and Marva's Vegan Jerky.

Our food is vegan, non GMO, straight from the farm, organic, healthy, pure, clean, made in small batches and earth friendly. We use no chemicals or artificial flavors and our product is 100% natural.

Our kitchen is yours.
Updates

Low designer entries

Target Market(s)

Vegetarians, vegans, health conscious, ecological, intelligent, caring.

Industry/Entity Type

Food Production

Logo Text

"Lonny and Marva" and "Our Kitchen is Yours"

Colors

Designer to choose colors to be used in the design.

Requirements
Must have
• earth friendly design, classy, hipster, vegan design, shabby chic,
Nice to have
• i have no ideas really...
• We prefer black and while, with a little splash of color. The last file is an idea I had but please use your own vision.

```html
<!DOCTYPE html>
<html lang="en">
<head>
<meta charset="utf-8">
<title>Lonny &amp; Marva's Vegan Jerky – Pouch Labels</title>
<link rel="stylesheet" href="https://fonts.googleapis.com/css2?family=Amatic+SC:wght@400;700&family=Kaushan+Script&family=Arimo:wght@400;700&display=swap">
<style>
  :root {
    --sage: #a7b49c;
    --leaf: #6b8f5c;
    --charcoal: #3d3d3d;
    --ink: #3a3a3a;
    --paper: #ffffff;
    --row: #e6e8e3;
  }
  * { margin: 0; padding: 0; box-sizing: border-box; }
  html, body { width: 1200px; height: 1000px; overflow: hidden; background: var(--paper); }
  .canvas { position: relative; width: 1200px; height: 1000px; font-family: "Arimo", Arial, sans-serif; color: var(--ink); }
  .abs { position: absolute; }
  .hand { font-family: "Amatic SC", "Arial Narrow", sans-serif; font-weight: 700; line-height: .9; text-transform: uppercase; white-space: nowrap; }
  .script { font-family: "Kaushan Script", cursive; line-height: 1; white-space: nowrap; color: var(--ink); }

  /* ---------- front label ---------- */
  .front-label { left: 104px; top: 142px; width: 449px; height: 715px; border: 1px solid #d6d6d6; overflow: hidden; }
  .front-band { left: 0; top: 0; width: 100%; height: 211px; background: var(--sage); }
  .logo-disc { border-radius: 50%; background: var(--charcoal); color: var(--paper); display: flex; align-items: center; justify-content: center; text-align: center; font-family: "Amatic SC", sans-serif; font-weight: 700; }
  .front-logo { left: 164px; top: 54px; width: 124px; height: 124px; font-size: 34px; line-height: .85; }
  .product-title { left: 0; top: 218px; width: 100%; text-align: center; font-size: 92px; font-weight: 400; }
  .flavor-tag { left: 61px; top: 358px; width: 107px; height: 104px; background: var(--leaf); color: var(--paper); font-size: 46px; font-weight: 400; letter-spacing: -1px; display: flex; align-items: center; justify-content: center; text-align: center; line-height: .92; }
  .word-healthy { left: 177px; top: 359px; font-size: 27px; letter-spacing: 4px; }
  .word-pure { left: 281px; top: 344px; font-size: 46px; }
  .word-nongmo { left: 176px; top: 390px; font-size: 87px; font-weight: 400; letter-spacing: 5px; }
  .word-farm { left: 63px; top: 472px; font-size: 30px; letter-spacing: 5.5px; }
  .claim-block { left: 61px; top: 510px; width: 52px; height: 166px; background: var(--charcoal); }
  .claim-block span { position: absolute; left: 50%; top: 50%; width: 166px; transform: translate(-50%,-50%) rotate(-90deg); color: var(--paper); display: flex; align-items: center; justify-content: center; gap: 4px; }
  .claim-no { font-size: 48px; }
  .claim-small { font-size: 20px; line-height: .9; text-align: left; }
  .word-organic { left: 128px; top: 500px; font-size: 46px; }
  .word-yummy { left: 128px; top: 532px; font-size: 160px; font-weight: 400; transform: scaleX(.58); transform-origin: left top; }
  .heart { left: 291px; top: 513px; width: 96px; height: 82px; }
  .heart-text { left: 291px; top: 534px; width: 96px; text-align: center; color: var(--paper); font-size: 19px; line-height: .95; }
  .word-hundred { left: 296px; top: 593px; font-size: 53px; font-weight: 400; letter-spacing: 6px; }
  .word-natural { left: 296px; top: 638px; font-size: 40px; font-weight: 400; letter-spacing: 2px; }

  /* ---------- back label ---------- */
  .back-label { left: 647px; top: 295px; width: 449px; height: 562px; border: 1px solid #d6d6d6; overflow: hidden; }
  .back-panel { left: 220px; top: 0; width: 229px; height: 100%; background: var(--charcoal); }
  .about-text { left: 110px; top: 60px; width: 94px; text-align: right; font-size: 34px; font-weight: 400; line-height: .92; }
  .story { left: 40px; top: 241px; width: 170px; text-align: right; font-size: 11px; line-height: 14.5px; }
  .story p + p { margin-top: 12px; }
  .back-logo { left: 133px; top: 463px; width: 76px; height: 76px; font-size: 22px; line-height: .85; }
  .net-weight { left: 20px; top: 531px; font-size: 16px; font-weight: 700; }
  .bag-heading { left: 245px; top: 101px; font-size: 36px; font-weight: 400; color: var(--paper); line-height: .9; }
  .ingredients { left: 239px; top: 213px; width: 170px; color: var(--paper); font-size: 11px; line-height: 14.5px; }
  .nutrition { left: 238px; top: 302px; width: 168px; height: 193px; background: var(--paper); padding: 5px 6px; font-size: 8px; line-height: 11px; }
  .nutrition h3 { font-size: 8.5px; letter-spacing: .5px; border-bottom: 1px solid var(--ink); padding-bottom: 3px; margin-bottom: 5px; }
  .nutrition .row { display: flex; justify-content: space-between; padding: 0 1px; }
  .nutrition .row.shade { background: var(--row); }
  .nutrition .row.indent span:first-child { padding-left: 8px; }
  .nutrition .group { border-bottom: 2px solid var(--ink); padding-bottom: 4px; margin-bottom: 4px; }
  .nutrition .values { border-bottom: 1px solid var(--ink); padding-bottom: 3px; }
  .nutrition .note { margin-top: 3px; font-size: 7.5px; line-height: 9px; }
  .best-before { left: 246px; top: 533px; color: var(--paper); font-size: 11px; }
  .date-box { left: 321px; top: 531px; width: 90px; height: 21px; background: var(--paper); font-size: 11px; text-align: center; line-height: 21px; }

  /* ---------- captions ---------- */
  .caption { top: 925px; font-size: 24px; font-weight: 700; color: #111; }
  .caption-front { left: 104px; }
  .caption-back { right: 100px; }
  .caption-rule { top: 964px; height: 1px; background: #999; }
</style>
</head>
<body>
<main class="canvas">

  <!-- Front label -->
  <section class="front-label abs" aria-label="Front label">
    <div class="front-band abs"></div>
    <svg class="abs" style="left:0;top:0" width="449" height="715" aria-hidden="true">
      <path d="M0 213 Q120 207 230 211 T449 208" fill="none" stroke="var(--ink)" stroke-width="1.6"/>
      <path d="M0 308 Q110 303 225 306 T449 302" fill="none" stroke="var(--ink)" stroke-width="1.6"/>
      <path d="M72 359 L79 343 L86 359 Z" fill="var(--leaf)"/>
    </svg>
    <div class="logo-disc front-logo abs">Lonny &amp;<br>Marva's</div>
    <h1 class="product-title hand abs">Vegan Jerky</h1>

    <div class="flavor-tag hand abs">Original<br>Flavor</div>
    <div class="word-healthy hand abs">Healthy</div>
    <div class="word-pure script abs">pure</div>
    <div class="word-nongmo hand abs">Non-GMO</div>
    <div class="word-farm hand abs">Straight from the farm</div>
    <div class="claim-block abs">
      <span class="hand"><b class="claim-no">No</b><b class="claim-small">Chemicals or<br>artificial flavors</b></span>
    </div>
    <div class="word-organic script abs">organic</div>
    <div class="word-yummy hand abs">Yummy</div>
    <svg class="heart abs" viewBox="0 0 98 84" aria-hidden="true">
      <path d="M49 82 C20 60 2 44 2 24 C2 10 13 1 26 1 C37 1 45 8 49 16 C53 8 61 1 72 1 C85 1 96 10 96 24 C96 44 78 60 49 82 Z" fill="var(--charcoal)"/>
    </svg>
    <div class="heart-text hand abs">Earth-<br>friendly</div>
    <div class="word-hundred hand abs">100%</div>
    <div class="word-natural hand abs">Natural</div>
  </section>

  <!-- Back label -->
  <section class="back-label abs" aria-label="Back label">
    <div class="back-panel abs"></div>
    <svg class="abs" style="left:0;top:0" width="449" height="562" aria-hidden="true">
      <path d="M110 52 L210 51 L211 199 L108 200 L108 88 L90 76 L109 70 Z" fill="var(--paper)" stroke="var(--ink)" stroke-width="1.5" stroke-linejoin="round"/>
      <path d="M233 92 L367 90 L366 170 L270 172 L258 190 L256 172 L234 172 Z" fill="var(--sage)" stroke="var(--paper)" stroke-width="1.5" stroke-linejoin="round"/>
      <path d="M0 522 Q110 518 220 520" fill="none" stroke="var(--ink)" stroke-width="1.5"/>
      <path d="M220 520 Q330 517 449 519" fill="none" stroke="var(--paper)" stroke-width="1.5"/>
    </svg>
    <div class="about-text hand abs">About<br>Lonny<br>&amp;<br>Marva's</div>
    <div class="story abs">
      <p>We are Lonny and Marva's. Cus quasped eos quam, qui optas di quiate eost eum illitis quiam, offictint, ullis dolupis quiatur, as molupta turibusa quia nis moloreris estiost.</p>
      <p>Moffictint, ullis dolupis quiatur, as molupta turibusa quia nis moloreris estiost, corrum, core, aut invendam fugitatius dolut faceresto tet que plit la doluptam.</p>
      <p>Our kitchen is yours.</p>
    </div>
    <div class="logo-disc back-logo abs">Lonny &amp;<br>Marva's</div>
    <div class="net-weight abs">000 g ℮</div>

    <h2 class="bag-heading hand abs">What's in<br>this bag?</h2>
    <div class="ingredients abs">Ingredients:<br>Icimusae (64%), sunduntum (20%), voluptae porem (8%), sitas, at re etur, voles, restium, endisqua - and nothing else!</div>
    <div class="nutrition abs">
      <h3>NUTRITION FACTS</h3>
      <div class="group">
        <div class="row"><span>Serving Size</span><span>...g</span></div>
        <div class="row"><span>Servings per Bag</span><span>...g</span></div>
      </div>
      <div class="values">
        <div class="row"><span>Calories ...</span><span>...%</span></div>
        <div class="row shade"><span>Total Fat ...g</span><span>...%</span></div>
        <div class="row indent"><span>Saturated Fat ...g</span><span>...%</span></div>
        <div class="row shade"><span>Cholesterol ...mg</span><span>...%</span></div>
        <div class="row"><span>Sodium ...mg</span><span>...%</span></div>
        <div class="row shade"><span>Total Carb ...g</span><span>...%</span></div>
        <div class="row indent"><span>Dietary Fiber ...g</span><span>...%</span></div>
        <div class="row shade indent"><span>Sugars ...g</span><span>...%</span></div>
        <div class="row"><span>Protein ...G</span><span>...%</span></div>
      </div>
      <p class="note">* Percent Daily Values are based on a 2,000 calorie diet.</p>
    </div>
    <div class="best-before abs">best before:</div>
    <div class="date-box abs">01.01.2099</div>
  </section>

  <div class="caption caption-front abs">Front Label</div>
  <div class="caption-rule abs" style="left:0;width:285px"></div>
  <div class="caption caption-back abs">Back Label</div>
  <div class="caption-rule abs" style="left:927px;width:273px"></div>

</main>
</body>
</html>
```